vQ CARELINE (Brochure Design)

i need a proffesional brochure made. we are a mobile medical service company providing mobile Arterial Blood Gases(ABG's). Respiratory & Ventilator Consultation services. Ventilator and Tracheostomy training courses. and mobile vaccine administration.

this is my first time making a brochure so any and all advice/guidance will be appreciated.

i am thinking prints will be 8.5 inches x 11 inches (TRI-FOLD and BI-FOLD)

i have uploaded my business card design and logo design for reference.
as this brochure project continues ill update needs of the project descriptions.

Introduction: At vq CARELINE, we're dedicated to enhancing healthcare services by providing exceptional mobile arterial blood gases, respiratory and ventilator consultation services. Our core values revolve around excellence, compassion and accessibility. We believe that every individual deserves the highest standard of care, and we're committed to delivering that through expert guidance and top-notch training courses. Your health is at the heart of what we do, and we're here to support you on your journey to better respiratory health.

Mobile Arterial Blood Gases : Our mobile Arterial Blood Gas service offers quick, on-the-spot analysis of pH, oxygen, and carbon dioxide levels in your the blood. This service enables rapid adjustments to treatment plans for more effective respiratory care.

Ventilator and Tracheostomy Training: Our ventilator and tracheostomy course empowers caregivers and healthcare professionals to manage ventilators and care for tracheostomy patients with expertise. This training enhances patient safety, treatment outcomes, and healthcare provider confidence. vQ Careline your choice for top-notch care, convenience, and peace of mind.

Respiratory Consulting: Our respiratory consulting services provide expert guidance and support for individuals with respiratory / ventilator concerns. Benefits include personalized treatment plans, better management of respiratory conditions, and improved overall lung health. vQ Careline is your trusted partner for a breath of fresh air.

Target Market(s)

Sub-Acute facilities, Pulmonary Clinics, Pulmonologists, Nurses, Caregivers, Hospice and homehealth companies.

Industry/Entity Type

Medical; Respiratory; Nursing

Requirements
Must have
• proffesional simple design.

```html
<!DOCTYPE html>
<html lang="en">
<head>
<meta charset="utf-8">
<title>vQ CARELINE Tri-fold Brochure</title>
<link href="https://fonts.googleapis.com/css2?family=Open+Sans:wght@400;600;700&family=Roboto+Condensed:wght@700&display=swap" rel="stylesheet">
<style>
  :root{
    --blue:#1565b8;
    --green:#8dc880;
    --white:#ffffff;
    --stage:#e6eaee;
    --photo-dark:#2c3442;
    --photo-skin:#d9b8a4;
    --photo-light:#dfe6ee;
    --device:#6f8fbf;
  }
  *{box-sizing:border-box;margin:0;padding:0}
  html,body{width:923px;height:1200px;overflow:hidden}
  body{background:var(--stage);font-family:"Open Sans",sans-serif;position:relative}
  .spread{position:absolute;left:112px;width:699px;height:539px;display:flex;box-shadow:0 4px 14px rgba(0,0,0,.18)}
  .spread--outside{top:46px}
  .spread--inside{top:620px}
  .panel{position:relative;width:233px;height:539px;overflow:hidden}
  .panel--white{background:var(--white)}
  .panel--blue{background:var(--blue)}
  .panel--green{background:var(--green)}
  .fill{position:absolute}
  .photo{position:absolute}
  .photo--device{background:linear-gradient(160deg,#e9eef6,var(--device) 60%,#dfe3ea);border-radius:10px}
  .photo--blood{left:0;top:0;width:233px;height:539px;background:linear-gradient(150deg,var(--photo-dark) 0 45%,var(--photo-skin) 70%,#eef2f4);clip-path:polygon(0 310px,142px 257px,233px 330px,233px 539px,0 539px)}
  .photo--patient{left:0;top:0;width:233px;height:539px;background:linear-gradient(135deg,#f5f7fa,var(--photo-light) 50%,#9fc0dd);clip-path:polygon(40px 108px,233px 108px,233px 334px,0 226px,0 200px)}
  .green-wedge{left:0;top:0;width:233px;height:539px;background:var(--green);clip-path:polygon(0 236px,233px 348px,233px 539px,0 539px)}
  .service{position:absolute;left:0;width:233px;text-align:center;color:var(--white);font-weight:700;font-size:14px;line-height:15px}
  .service-icon{display:block;margin:0 auto 6px}
  .abg-box{position:absolute;left:60px;top:152px;width:113px;height:112px;border:1.5px solid var(--white);border-radius:8px;padding-top:16px}
  .abg-box .service{position:static;width:auto}
  .contact{position:absolute;left:0;top:424px;width:233px;text-align:center;color:var(--white);font-weight:600;font-size:10.4px;line-height:16px;letter-spacing:.3px}
  .contact-icons{display:flex;justify-content:center;gap:6px;margin-bottom:9px}
  .brand{position:absolute;display:flex;align-items:center;gap:7px;font-weight:400;font-size:17px;letter-spacing:.2px}
  .brand-mark{width:30px;height:30px}
  .brand--blue{left:44px;top:44px;color:var(--blue)}
  .brand--blue .brand-mark{background:var(--blue)}
  .brand--white{left:42px;top:420px;color:var(--white)}
  .brand--white .brand-mark{background:var(--white)}
  .headline{position:absolute;left:21px;width:200px;font-family:"Roboto Condensed",sans-serif;font-weight:700;font-size:16.5px;line-height:19.5px;color:var(--white)}
  .copy{position:absolute;left:21px;width:196px;font-size:10px;line-height:12.8px;color:var(--white)}
  .copy-title{position:absolute;left:21px;font-size:10px;font-weight:700;color:var(--white)}
</style>
</head>
<body>

<!-- Outside of brochure -->
<section class="spread spread--outside">
  <div class="panel panel--white">
    <div class="photo photo--device" style="left:22px;top:52px;width:192px;height:118px" role="img" aria-label="Two portable ventilator units"></div>
    <div class="photo photo--blood" role="img" aria-label="Gloved hands drawing an arterial blood sample with a syringe"></div>
  </div>

  <div class="panel panel--blue">
    <svg class="fill" width="233" height="539" viewBox="0 0 233 539" style="left:0;top:0">
      <polygon points="0,337 116.5,406 233,337 233,539 0,539" fill="#ffffff"/>
      <polygon points="0,348 116.5,417 233,348 233,539 0,539" fill="#8dc880"/>
    </svg>
    <div class="service" style="top:50px">
      <svg class="service-icon" width="46" height="46" viewBox="0 0 46 46"><circle cx="23" cy="23" r="21.5" fill="none" stroke="#fff" stroke-width="1.5"/><ellipse cx="17" cy="25" rx="6" ry="9" fill="#fff"/><ellipse cx="29" cy="25" rx="6" ry="9" fill="#fff"/><rect x="22" y="11" width="2" height="10" fill="#fff"/></svg>
      Respiratory<br>Consultations
    </div>
    <div class="abg-box">
      <div class="service">
        <svg class="service-icon" width="46" height="46" viewBox="0 0 46 46"><circle cx="23" cy="23" r="21.5" fill="none" stroke="#fff" stroke-width="1.5"/><rect x="20" y="10" width="7" height="24" rx="1.5" fill="#fff" transform="rotate(-40 23 23)"/><rect x="22.5" y="32" width="2" height="7" fill="#fff" transform="rotate(-40 23 23)"/></svg>
        In-house<br>ABG's
      </div>
    </div>
    <div class="service" style="top:293px">
      <svg class="service-icon" width="30" height="30" viewBox="0 0 30 30"><rect x="6" y="3" width="14" height="12" rx="1.5" fill="none" stroke="#fff" stroke-width="1.5"/><rect x="9" y="6" width="8" height="5" fill="#fff"/><line x1="13" y1="15" x2="13" y2="25" stroke="#fff" stroke-width="1.5"/><line x1="7" y1="25" x2="19" y2="25" stroke="#fff" stroke-width="1.5"/><circle cx="23" cy="15" r="3" fill="#fff"/></svg>
      Ventilator<br>Training
    </div>
    <div class="contact">
      <div class="contact-icons">
        <svg width="12" height="12" viewBox="0 0 12 12"><path d="M2 1h2.5l1 2.8-1.4 1a6 6 0 0 0 3 3l1-1.4 2.9 1V10a1 1 0 0 1-1 1A9 9 0 0 1 1 2a1 1 0 0 1 1-1z" fill="#fff"/></svg>
        <svg width="12" height="12" viewBox="0 0 12 12"><rect x="1" y="5" width="10" height="6" fill="#fff"/><rect x="3" y="1" width="6" height="4" fill="none" stroke="#fff"/></svg>
        <svg width="12" height="12" viewBox="0 0 12 12"><rect x="0.5" y="2.5" width="11" height="7.5" fill="#fff"/><path d="M1 3l5 4 5-4" fill="none" stroke="#1565b8"/></svg>
        <svg width="12" height="12" viewBox="0 0 12 12"><circle cx="6" cy="6" r="5" fill="none" stroke="#fff"/><ellipse cx="6" cy="6" rx="2.2" ry="5" fill="none" stroke="#fff"/><line x1="1" y1="6" x2="11" y2="6" stroke="#fff"/></svg>
      </div>
      555.010.2994<br>555.014.2223<br>info@vqcarelinegroup.com<br>vqcarelinegroup.com
    </div>
  </div>

  <div class="panel panel--white">
    <div class="brand brand--blue"><span class="brand-mark"></span>vQ CARELINE</div>
    <div class="photo photo--patient" role="img" aria-label="Patient resting in a hospital bed with a nurse beside him"></div>
    <div class="fill green-wedge"></div>
    <p class="headline" style="top:343px">Respiratory &amp; Ventilator Consultation services.</p>
    <p class="headline" style="top:400px">Ventilator and Tracheostomy training courses.</p>
    <p class="headline" style="top:462px">Mobile vaccine administration.</p>
  </div>
</section>

<!-- Inside of brochure -->
<section class="spread spread--inside">
  <div class="panel panel--blue">
    <p class="copy" style="top:36px">At vq CARELINE, we're dedicated to enhancing healthcare services by providing exceptional mobile arterial blood gases, respiratory and ventilator consultation services. Our core values revolve around excellence, compassion and accessibility. We believe that every individual deserves the highest standard of care, and we're committed to delivering that through expert guidance and top-notch training courses. Your health is at the heart of what we do, and we're here to support you on your journey to better respiratory health.</p>
    <svg class="fill" width="233" height="80" viewBox="0 0 233 80" style="left:0;top:207px">
      <polyline points="0,2 116.5,72 233,2" fill="none" stroke="#fff" stroke-width="7"/>
    </svg>
    <p class="copy-title" style="top:298px">Mobile Arterial Blood Gases :</p>
    <p class="copy" style="top:323px">Our mobile Arterial Blood Gas service offers quick, on-the-spot analysis of pH, oxygen, and carbon dioxide levels in your the blood. This service enables rapid adjustments to treatment plans for more effective respiratory care.</p>
    <div class="photo" style="left:0;top:416px;width:233px;height:123px;background:linear-gradient(120deg,#3b6fc4,#e8d2c4 55%,#f2f2f2)" role="img" aria-label="Blue-gloved hands taking a blood sample from an arm"></div>
  </div>

  <div class="panel panel--green">
    <svg class="fill" width="233" height="243" viewBox="0 0 233 243" style="left:0;top:0">
      <polygon points="68,0 233,0 233,243 68,243 0,106" fill="#ffffff"/>
    </svg>
    <div class="photo photo--device" style="left:38px;top:40px;width:170px;height:186px" role="img" aria-label="Portable ventilator with a touchscreen display"></div>
    <p class="copy-title" style="top:275px">Ventilator and Tracheostomy Training:</p>
    <p class="copy" style="top:301px">Our ventilator and tracheostomy course empowers caregivers and healthcare professionals to manage ventilators and care for tracheostomy patients with expertise. This training enhances patient safety, treatment outcomes, and healthcare provider confidence. vQ Careline your choice for top-notch care, convenience, and peace of mind.</p>
    <div class="brand brand--white"><span class="brand-mark"></span>vQ CARELINE</div>
  </div>

  <div class="panel panel--green">
    <p class="copy-title" style="top:30px">Respiratory Consulting:</p>
    <p class="copy" style="top:56px">Our respiratory consulting services provide expert guidance and support for individuals with respiratory / ventilator concerns. Benefits include personalized treatment plans, better management of respiratory conditions, and improved overall lung health. vQ Careline is your trusted partner for a breath of fresh air.</p>
    <div class="photo" style="left:29px;top:249px;width:175px;height:245px;background:linear-gradient(180deg,#4a3f8f 0 6%,#eef0f2 8%,#e4e6e8 92%,#4a3f8f 94%);border-radius:6px" role="img" aria-label="Upright ventilator unit with control keypad"></div>
  </div>
</section>

</body>
</html>
```